Brochure design for garden shed range for www.yardcabins2go.ie

we want to have a brochure designed for our products at www.yardcabins2go.ie
this should clearly show the ranges of products we sell and there features it wont need all our pricing but more to show our quality of products. We can work together with designers to get the right information on all our ranges and any text needed for the brochure.

Target Market(s)

general public

Industry/Entity Type

Home And Garden

```html
<!DOCTYPE html>
<html lang="en">
<head>
<meta charset="utf-8">
<title>Yard Cabins 2 Go – Garden Shed Range</title>
<link href="https://fonts.googleapis.com/css2?family=Cormorant+Garamond:wght@600&family=Open+Sans:wght@400;700&display=swap" rel="stylesheet">
<style>
  :root {
    --green-dark: #0f3a12;
    --green-bar: #12401a;
    --olive: #4f6b12;
    --olive-light: #7f9a2c;
    --card-grey: #ececec;
    --card-grey-light: #f6f6f6;
    --badge-grey: #d9d9d9;
    --text: #1e1e1e;
    --white: #ffffff;
    --wood-warm: #b7773d;
    --wood-deep: #7e4a22;
    --wood-pale: #d8c9a3;
    --lawn: #5f7d3a;
  }
  * { box-sizing: border-box; margin: 0; padding: 0; }
  html, body { width: 1200px; height: 800px; overflow: hidden; background: var(--white); }
  body { font-family: "Open Sans", Arial, sans-serif; color: var(--text); position: relative; }

  .range-grid {
    position: absolute; left: 22px; top: 22px;
    width: 1156px;
    display: grid;
    grid-template-columns: repeat(3, 368px);
    grid-template-rows: repeat(4, 160px);
    column-gap: 26px; row-gap: 20px;
  }

  .shed-card { display: flex; flex-direction: column; }
  .shed-card__title {
    height: 34px; background: var(--green-dark); color: var(--white);
    border-radius: 12px 12px 0 0;
    font-family: "Cormorant Garamond", Georgia, serif; font-weight: 600;
    font-size: 27px; line-height: 34px; text-align: center; padding-left: 40px;
  }
  .shed-card__body {
    position: relative; flex: 1;
    background: linear-gradient(180deg, var(--card-grey-light), var(--card-grey));
    border-radius: 0 0 14px 14px; overflow: hidden;
  }
  .shed-card__photo {
    position: absolute; left: 0; top: 0; bottom: 0; width: 200px;
    background:
      linear-gradient(90deg, rgba(236,236,236,0) 55%, var(--card-grey) 100%),
      linear-gradient(180deg, #c9d3dc 0%, #c9d3dc 18%, var(--wood-warm) 19%, var(--wood-deep) 80%, var(--lawn) 100%);
  }
  .shed-card__photo--pale {
    background:
      linear-gradient(90deg, rgba(236,236,236,0) 55%, var(--card-grey) 100%),
      linear-gradient(180deg, #cdd6de 0%, #cdd6de 18%, var(--wood-pale) 19%, #b8a77f 82%, #6b6b5e 100%);
  }
  .shed-card__price {
    position: absolute; left: 0; bottom: 12px;
    width: 150px; height: 24px; padding-left: 16px;
    background: linear-gradient(90deg, var(--olive), var(--olive-light) 80%, rgba(127,154,44,0));
    color: var(--white); font-weight: 700; font-size: 12.5px; line-height: 24px;
  }
  .shed-card__features {
    position: absolute; left: 184px; top: 7px; right: 8px;
    font-size: 12.4px; line-height: 14.4px;
  }
  .shed-card__features h3 { font-size: 12.6px; font-weight: 700; }
  .shed-card__features ul { list-style: none; }
  .shed-card__features li { padding-left: 11px; position: relative; }
  .shed-card__features li::before {
    content: ""; position: absolute; left: 2px; top: 6px;
    width: 4px; height: 4px; background: var(--text);
  }

  .brand-panel {
    position: relative; display: flex; flex-wrap: wrap;
    align-items: center; align-content: center; gap: 22px 24px; padding-left: 14px;
  }
  .brand-name {
    display: flex; align-items: center; gap: 10px;
    font-weight: 700; font-size: 20px; color: var(--green-dark);
  }
  .brand-name__mark { width: 18px; height: 18px; background: var(--green-dark); }
  .partner-badge { display: block; width: 90px; height: 44px; background: var(--badge-grey); }
</style>
</head>
<body>
<main class="range-grid">

  <article class="shed-card">
    <h2 class="shed-card__title">Premium Standard</h2>
    <div class="shed-card__body">
      <div class="shed-card__photo" role="img" aria-label="Photo of a premium standard apex shed with glazed windows"></div>
      <div class="shed-card__price">From €499.99</div>
      <div class="shed-card__features"><h3>Product Features</h3><ul>
        <li>Shiplap Siding</li><li>T&amp;G Roof &amp; Floor</li><li>TimberShield Treated</li>
        <li>Glazed Windows</li><li>Heavy Duty Felt Roof</li><li>Free Fitting &amp; Delivery</li></ul></div>
    </div>
  </article>

  <article class="shed-card">
    <h2 class="shed-card__title">Premium Lean</h2>
    <div class="shed-card__body">
      <div class="shed-card__photo" role="img" aria-label="Photo of a premium lean-to shed"></div>
      <div class="shed-card__price">From €349.99</div>
      <div class="shed-card__features"><h3>Product Features</h3><ul>
        <li>Shiplap Siding</li><li>TimberShield Treated</li><li>T&amp;G Floor and Roof</li>
        <li>Galvanised Nailed</li><li>90lb Felt Roof Membrane</li></ul></div>
    </div>
  </article>

  <article class="shed-card">
    <h2 class="shed-card__title">Potting Sheds</h2>
    <div class="shed-card__body">
      <div class="shed-card__photo" role="img" aria-label="Photo of a potting shed with many windows"></div>
      <div class="shed-card__price">From €549.00</div>
      <div class="shed-card__features"><h3>Product Features</h3><ul>
        <li>Shiplap Siding</li><li>TimberShield Treated</li><li>T&amp;G Floor and Roof</li>
        <li>Galvanised Nailed</li><li>90lb Felt Roof Menbrane</li></ul></div>
    </div>
  </article>

  <article class="shed-card">
    <h2 class="shed-card__title">Premium Kendal</h2>
    <div class="shed-card__body">
      <div class="shed-card__photo" role="img" aria-label="Photo of a premium Kendal shed with two windows"></div>
      <div class="shed-card__price">From €479.99</div>
      <div class="shed-card__features"><h3>Product Features</h3><ul>
        <li>T&amp;G Floor and roof</li><li>Shiplap Siding</li><li>Glazed windows</li>
        <li>TimberShield Treated</li><li>Galavanised Fitting</li><li>Free home delivery</li></ul></div>
    </div>
  </article>

  <article class="shed-card">
    <h2 class="shed-card__title">Overlap Lean</h2>
    <div class="shed-card__body">
      <div class="shed-card__photo shed-card__photo--pale" role="img" aria-label="Photo of an overlap lean-to shed"></div>
      <div class="shed-card__price">From €339.00</div>
      <div class="shed-card__features"><h3>Product Features</h3><ul>
        <li>Fully Pressure Treated</li><li>Overlap Siding</li><li>Galvanised Nailed</li>
        <li>Free Delivery &amp; Fitting</li><li>90lb Felt Roof Membrane</li></ul></div>
    </div>
  </article>

  <article class="shed-card">
    <h2 class="shed-card__title">Kids Playhouse</h2>
    <div class="shed-card__body">
      <div class="shed-card__photo" role="img" aria-label="Photo of a kids wooden playhouse on a lawn"></div>
      <div class="shed-card__price">From €449.99</div>
      <div class="shed-card__features"><h3>Product Features</h3><ul>
        <li>Shiplap Siding</li><li>Arched Glazed windows</li><li>Stable Door</li>
        <li>TimberShield Treated</li><li>90lb Felt Roof Membrane</li><li>Free Delivery &amp; Fitting</li></ul></div>
    </div>
  </article>

  <article class="shed-card">
    <h2 class="shed-card__title">Premium Lodge</h2>
    <div class="shed-card__body">
      <div class="shed-card__photo" role="img" aria-label="Photo of a premium lodge shed"></div>
      <div class="shed-card__price">From €599.99</div>
      <div class="shed-card__features"><h3>Product Features</h3><ul>
        <li>Shiplap Siding</li><li>T&amp;G roof and floorng</li><li>Galavanised Fittings</li>
        <li>TimberShield Treated</li><li>Free Home delivery</li></ul></div>
    </div>
  </article>

  <article class="shed-card">
    <h2 class="shed-card__title">Overlap Standard</h2>
    <div class="shed-card__body">
      <div class="shed-card__photo shed-card__photo--pale" role="img" aria-label="Photo of an overlap standard apex shed"></div>
      <div class="shed-card__price">From €399.99</div>
      <div class="shed-card__features"><h3>Product Features</h3><ul>
        <li>Overlap Siding</li><li>Fully Pressure treated</li><li>Free delivery &amp; fitting</li>
        <li>Galvanised fittings &amp; fixings</li><li>Glazed windows</li></ul></div>
    </div>
  </article>

  <article class="shed-card">
    <h2 class="shed-card__title">Kids Tree House</h2>
    <div class="shed-card__body">
      <div class="shed-card__photo" role="img" aria-label="Photo of a raised kids tree house with ladder"></div>
      <div class="shed-card__price">From €799.99</div>
      <div class="shed-card__features"><h3>Product Features</h3><ul>
        <li>Shiplap Siding</li><li>3ft Stand</li><li>Stable Door</li>
        <li>TimberShield Treated</li><li>90lb Felt Roof Membrane</li><li>Free Delivery &amp; Fitting</li></ul></div>
    </div>
  </article>

  <article class="shed-card">
    <h2 class="shed-card__title">Summer Chalet</h2>
    <div class="shed-card__body">
      <div class="shed-card__photo" role="img" aria-label="Photo of a summer chalet with veranda among trees"></div>
      <div class="shed-card__price">From €629.00</div>
      <div class="shed-card__features"><h3>Product Features</h3><ul>
        <li>18mm Shiplap Siding</li><li>T&amp;G Roof and Floor</li><li>Free Fitting &amp; Delivery</li>
        <li>TimberShield Treated</li><li>Galavanised Nailed</li><li>30" Veranda</li></ul></div>
    </div>
  </article>

  <article class="shed-card">
    <h2 class="shed-card__title">Overlap Kendal</h2>
    <div class="shed-card__body">
      <div class="shed-card__photo shed-card__photo--pale" role="img" aria-label="Photo of an overlap Kendal shed in a back garden"></div>
      <div class="shed-card__price">From €479.99</div>
      <div class="shed-card__features"><h3>Product Features</h3><ul>
        <li>Overlap Rustic Siding</li><li>Pressure treated</li><li>Galvanized fittings</li>
        <li>Georgian style windows</li><li>Internal Membrane</li></ul></div>
    </div>
  </article>

  <aside class="brand-panel">
    <div class="brand-name"><span class="brand-name__mark"></span>Yard Cabins 2 Go</div>
    <span class="partner-badge" aria-hidden="true"></span>
    <span class="partner-badge" aria-hidden="true"></span>
  </aside>

</main>

<footer class="warranty-bar" style="position:absolute;left:0;right:0;bottom:0;height:48px;background:var(--green-bar);color:var(--white);font-weight:700;font-size:20px;line-height:48px;text-align:center;letter-spacing:0.2px;">CALL TODAY TO GET OUR LIFETIME WARRANTY</footer>
</body>
</html>
```